Contemporary update for a market leader in foodservice distribution

KORVELT is a market leader in foodservice distribution nationwide.
We have recently adopted a new look and feel for our flagship foodservice rewards programme, and we're looking to have our business cards reflect our new aesthetic. Below is a link to our new rewards website to give you a general idea on the look we're after. https://korveltperks.com.au/

Industry/Entity Type

Distribution

Contact Information for Business Card

Must have space for contact name, position, company name and ABN, address, phone number and direct number, fax, email, and web address.

Font styles to use
Serif
Sans Serif

Requirements
Must have
• We'd like a landscape design, with our 'Tip of the Peak' logo incorporated on either the front or the back of the card. The overall design should be contemporary and professional.
Nice to have
• I have included both the full colour and white version of our company logo - our preference is to have the company logo one solid colour (white, or a shade of grey) although we're also open to designs including the full colour logo. If you are able to incorporate a small Facebook and LinkedIn logo, please do so.
Should not have
• Should not have an over-complicated design. No images of globes, or food.

```html
<!DOCTYPE html>
<html lang="en">
<head>
<meta charset="utf-8">
<title>KORVELT Business Card</title>
<link href="https://fonts.googleapis.com/css2?family=Marcellus&family=Roboto:wght@400;500&family=Saira+Condensed:wght@700&display=swap" rel="stylesheet">
<style>
  :root {
    --canvas: #dcdcdc;
    --ink: #222222;
    --ink-soft: #3a3a3a;
    --green: #1e9a5c;
    --green-dark: #137a45;
    --charcoal: #1c1c1c;
    --slate: #4a4a4a;
    --paper: #ffffff;
    --rule: #2b2b2b;
  }
  * { box-sizing: border-box; margin: 0; padding: 0; }
  html, body { width: 1200px; height: 1200px; overflow: hidden; background: var(--canvas); }
  body { position: relative; font-family: "Roboto", Arial, sans-serif; color: var(--ink); }

  .card {
    position: absolute; left: 150px; width: 900px; height: 515px;
    border-radius: 26px; overflow: hidden;
    box-shadow: 0 14px 30px rgba(0,0,0,0.22);
  }
  .card--front { top: 55px; background: var(--charcoal); }
  .card--back { top: 625px; background: var(--paper); }

  .card__photo {
    position: absolute; inset: 0;
    background: radial-gradient(ellipse at 55% 35%, #4a4a4a 0%, #2c2c2c 45%, #151515 100%);
  }
  .card__shapes { position: absolute; inset: 0; }

  .brand { position: absolute; display: flex; align-items: center; gap: 18px; }
  .brand__dot { width: 58px; height: 58px; border-radius: 50%; background: var(--green); flex: none; }
  .brand__name { font-family: "Marcellus", Georgia, serif; font-size: 76px; line-height: 1; letter-spacing: 2px; }
  .card--front .brand { left: 210px; top: 180px; }
  .card--front .brand__name { color: #ffffff; }
  .card--back .brand { left: 55px; top: 90px; }
  .card--back .brand__dot { width: 48px; height: 48px; }
  .card--back .brand__name { font-size: 62px; color: var(--ink); }

  .abn-front { position: absolute; right: 40px; top: 398px; color: #ffffff; font-size: 23px; letter-spacing: 1px; }

  .social { position: absolute; left: 40px; bottom: 52px; display: flex; align-items: center; gap: 12px; color: #ffffff; font-size: 22px; letter-spacing: 1px; }
  .social__icon { width: 30px; height: 30px; border-radius: 5px; background: var(--green); }

  .programme { position: absolute; right: 60px; top: 60px; display: flex; align-items: center; gap: 12px; }
  .programme__dot { width: 40px; height: 40px; border-radius: 50%; background: var(--green); }
  .programme__name { font-family: "Saira Condensed", "Arial Narrow", sans-serif; font-size: 44px; color: var(--ink); line-height: 1; }

  .divider { position: absolute; left: 330px; right: 40px; top: 250px; height: 1.5px; background: var(--rule); }

  .company-details { position: absolute; right: 40px; top: 272px; text-align: right; font-size: 21px; line-height: 1.3; color: var(--ink-soft); }
  .company-details__abn { color: var(--green); font-size: 22px; }

  .person { position: absolute; left: 58px; top: 280px; }
  .person__name { font-family: "Saira Condensed", "Arial Narrow", sans-serif; color: var(--green); font-size: 36px; line-height: 1.05; }
  .person__role { font-size: 20px; color: var(--ink-soft); }

  .contacts { position: absolute; left: 58px; top: 362px; list-style: none; }
  .contacts__item { display: flex; align-items: center; gap: 18px; font-size: 21px; line-height: 28px; color: var(--ink); }
  .contacts__item svg { width: 18px; height: 18px; fill: var(--green-dark); flex: none; }

  .web { position: absolute; right: 40px; bottom: 24px; color: #ffffff; font-size: 20px; letter-spacing: 0.5px; }
</style>
</head>
<body>

<section class="card card--front" aria-label="Card front">
  <div class="card__photo" role="img" aria-label="Dark monochrome photograph of a foodservice warehouse setting"></div>
  <svg class="card__shapes" viewBox="0 0 900 515" aria-hidden="true">
    <polygon points="510,380 900,380 900,445 500,445" fill="var(--green)"/>
    <rect x="0" y="445" width="900" height="70" fill="rgba(20,20,20,0.55)"/>
  </svg>
  <div class="brand">
    <span class="brand__dot"></span>
    <span class="brand__name">KORVELT</span>
  </div>
  <p class="abn-front">ABN: 112233445566</p>
  <div class="social">
    <span>Find us on:</span>
    <span class="social__icon" role="img" aria-label="Social profile link"></span>
    <span class="social__icon" role="img" aria-label="Social profile link"></span>
  </div>
</section>

<section class="card card--back" aria-label="Card back">
  <svg class="card__shapes" viewBox="0 0 900 515" aria-hidden="true">
    <polygon points="0,490 510,470 500,515 0,515" fill="var(--green)"/>
    <polygon points="540,440 900,440 900,515 515,515" fill="var(--slate)"/>
  </svg>

  <div class="brand">
    <span class="brand__dot"></span>
    <span class="brand__name">KORVELT</span>
  </div>

  <div class="programme">
    <span class="programme__dot"></span>
    <span class="programme__name">Tip of the Peak</span>
  </div>

  <div class="divider"></div>

  <div class="company-details">
    <p class="company-details__abn">ABN: 112233445566</p>
    <p>Your Long Commercial or</p>
    <p>business address in 2 line</p>
  </div>

  <div class="person">
    <p class="person__name">Your Good Name</p>
    <p class="person__role">Managing Director</p>
  </div>

  <ul class="contacts">
    <li class="contacts__item">
      <svg viewBox="0 0 24 24"><path d="M6.6 10.8a15.1 15.1 0 0 0 6.6 6.6l2.2-2.2a1 1 0 0 1 1-.25 11.4 11.4 0 0 0 3.6.57 1 1 0 0 1 1 1V20a1 1 0 0 1-1 1A17 17 0 0 1 3 4a1 1 0 0 1 1-1h3.5a1 1 0 0 1 1 1c0 1.25.2 2.45.57 3.57a1 1 0 0 1-.25 1z"/></svg>
      +00 111 222 3333
    </li>
    <li class="contacts__item">
      <svg viewBox="0 0 24 24"><path d="M3 8c0-2 4-4 9-4s9 2 9 4v2h-5V8H8v2H3zM6 12h12l2 8H4z"/></svg>
      +00 222 333 4444
    </li>
    <li class="contacts__item">
      <svg viewBox="0 0 24 24"><path d="M7 3h10v5H7zM4 9h16v8h-3v4H7v-4H4zM9 15v4h6v-4z"/></svg>
      +00 555 666 7777
    </li>
    <li class="contacts__item">
      <svg viewBox="0 0 24 24"><path d="M2 5h20v14H2zM4 7v.5l8 5 8-5V7l-8 5z"/></svg>
      info@korveltperks.com.au
    </li>
  </ul>

  <p class="web">www.korveltperks.com.au</p>
</section>

</body>
</html>
```